Stationary Design Letterhead and Envelope

Artist should provide Letterhead and envelop stationary designs

Info for stationary:
Fernhallow Outdoor Advertising
4873 Quarry Rd. 915 N. PO BOX 528617
Austin, TX 78519

Dale Fernhallow
President
555-862-1907
dale@fernhallowsigns.example
fernhallowsigns.example

Target Market(s)

clients

Colors
0054AA
0677BA
7BADD7
CADEEF
E8F1F8

Requirements
Must have
• high quality unique eye catching and dynamic

```html
<!DOCTYPE html>
<html lang="en">
<head>
<meta charset="utf-8">
<title>Fernhallow Outdoor Advertising – Stationery</title>
<link rel="stylesheet" href="https://fonts.googleapis.com/css2?family=Open+Sans:wght@400;700&family=Josefin+Sans:wght@400;600&family=Arimo:wght@400&display=swap">
<style>
  :root {
    --brand-blue: #0b63a0;
    --brand-black: #111111;
    --paper: #e6e6e6;
    --ground: #f2f2f2;
    --ink: #1a1a1a;
    --grey-text: #7a7a7a;
    --card-dark: #0d0d0d;
    --logo-dim: #3a3a3a;
  }
  * { box-sizing: border-box; margin: 0; padding: 0; }
  html, body { width: 1200px; height: 932px; overflow: hidden; background: var(--ground); }
  .canvas { position: relative; width: 1200px; height: 932px; }

  .sheet { position: absolute; background: var(--paper); box-shadow: 0 1px 4px rgba(0,0,0,.18); overflow: hidden; }

  /* wordmark */
  .wordmark { position: absolute; display: flex; align-items: center; gap: 6px;
    font-family: "Open Sans", sans-serif; font-weight: 700; color: var(--ink); line-height: 1; white-space: nowrap; }
  .wordmark .mark-square { background: var(--brand-blue); flex: none; }
  .wordmark.on-blue { color: #fff; }
  .wordmark.on-blue .mark-square { background: #fff; }
  .wordmark.on-dark { color: var(--logo-dim); }
  .wordmark.on-dark .mark-square { background: var(--logo-dim); }

  .address { position: absolute; font-family: "Josefin Sans", sans-serif; color: var(--ink); white-space: nowrap; }
  .address .company { color: var(--brand-blue); font-weight: 600; }

  .footer-band { position: absolute; left: 0; right: 0; display: flex; font-family: "Josefin Sans", sans-serif; color: #fff; }
  .footer-band .contact { background: var(--brand-blue); display: flex; align-items: center; gap: 14px;
    clip-path: polygon(0 0, 100% 0, calc(100% - 12px) 100%, 0 100%); }
  .footer-band .web { background: var(--brand-black); flex: 1; display: flex; align-items: center; justify-content: center; margin-left: -8px;
    clip-path: polygon(12px 0, 100% 0, 100% 100%, 0 100%); }
  .footer-band .item { display: flex; align-items: center; gap: 6px; }
  .footer-band svg { flex: none; }

  /* letterhead */
  .letterhead { left: 65px; top: 88px; width: 567px; height: 732px; }
  .letterhead .wordmark { left: 31px; top: 38px; font-size: 33px; }
  .letterhead .wordmark .mark-square { width: 22px; height: 22px; }
  .letterhead .address { left: 351px; top: 39px; font-size: 11.5px; line-height: 13.5px; }
  .letter { font-family: "Arimo", sans-serif; color: var(--grey-text); }
  .meta { position: absolute; top: 186px; font-size: 9px; line-height: 12px; }
  .meta .label { color: var(--ink); font-size: 9.5px; }
  .meta.subject { left: 166px; }
  .meta.date { left: 466px; top: 184px; }
  .salutation { position: absolute; left: 166px; top: 261px; font-size: 12px; color: #6f6f6f; }
  .body-copy { position: absolute; left: 166px; top: 288px; width: 347px; font-size: 9.1px; line-height: 12.25px; text-align: justify; }
  .body-copy p { margin-bottom: 12.25px; }
  .side-note { position: absolute; right: 445px; top: 319px; text-align: right; font-size: 9px; line-height: 12px; }
  .side-note p { margin-bottom: 7px; }
  .side-note .dark { color: var(--ink); }
  .signature { position: absolute; left: 166px; top: 550px; font-size: 12px; line-height: 14.5px; color: #6f6f6f; }
  .letterhead .footer-band { top: 695px; height: 23px; font-size: 10px; }
  .letterhead .footer-band .contact { width: 382px; padding-left: 24px; }

  /* business cards */
  .card-front { left: 657px; top: 89px; width: 241px; height: 137px; }
  .card-front .wordmark { left: 14px; top: 14px; font-size: 19px; gap: 4px; }
  .card-front .wordmark .mark-square { width: 12px; height: 12px; }
  .card-person { position: absolute; left: 14px; top: 64px; font-family: "Open Sans", sans-serif; }
  .card-person .name { font-size: 8.5px; font-weight: 700; color: var(--ink); }
  .card-person .name .first { color: var(--brand-blue); }
  .card-person .role { font-size: 6.5px; color: #444; margin-top: 1px; }
  .card-contact { position: absolute; left: 14px; top: 93px; font-family: "Josefin Sans", sans-serif; font-size: 5.5px; color: var(--ink); line-height: 8.5px; }
  .card-contact .item { display: flex; align-items: center; gap: 3px; }
  .card-front .footer-band { top: 118px; height: 10px; font-size: 5.3px; }
  .card-front .footer-band .contact { width: 168px; padding-left: 8px; }

  .card-back { left: 908px; top: 89px; width: 241px; height: 137px; background: var(--card-dark); }
  .card-back .wordmark { left: 50%; top: 50%; transform: translate(-50%, -50%); font-size: 21px; gap: 5px; }
  .card-back .wordmark .mark-square { width: 13px; height: 13px; }

  /* envelope front */
  .envelope-front { left: 657px; top: 281px; width: 487px; height: 241px; }
  .envelope-front .wordmark { left: 24px; top: 23px; font-size: 27px; }
  .envelope-front .wordmark .mark-square { width: 18px; height: 18px; }
  .envelope-front .address { left: 29px; top: 155px; font-size: 8.6px; line-height: 11px; }
  .envelope-front .footer-band { top: 209px; height: 19px; font-size: 8.4px; }
  .envelope-front .footer-band .contact { width: 327px; padding-left: 28px; }

  /* envelope back */
  .envelope-back { left: 657px; top: 580px; width: 487px; height: 242px; background: transparent; box-shadow: none; overflow: visible; }
  .envelope-back > svg { position: absolute; inset: 0; }
  .envelope-back .wordmark { left: 50%; top: 21px; transform: translateX(-50%); font-size: 25px; }
  .envelope-back .wordmark .mark-square { width: 16px; height: 16px; }
</style>
</head>
<body>
<main class="canvas">

  <!-- Letterhead -->
  <section class="sheet letterhead" aria-label="Letterhead">
    <div class="wordmark"><span class="mark-square"></span>FERNHALLOW</div>
    <div class="address">
      <div class="company">Fernhallow Outdoor Advertising</div>
      <div>4873 Quarry Rd. 915 N. PO BOX 528617</div>
      <div>Austin, TX 78519</div>
    </div>

    <div class="letter">
      <div class="meta subject"><div class="label">SUBJECT :</div><div>Lorem Ipsum is simply dummy</div></div>
      <div class="meta date"><div class="label">DATE :</div><div>15-09-2017</div></div>

      <div class="side-note">
        <p><span class="dark">Lorem Ipsum is<br>simply dummy text<br>of the printing</span></p>
        <p><span class="dark">Lorem Ipsum is</span><br>simply dummy text</p>
      </div>

      <div class="salutation">Dear Person,</div>
      <div class="body-copy">
        <p>Lorem Ipsum is simply dummy text of the printing and typesetting industry. Lorem Ipsum has been the industry's standard dummy text ever since the 1500s, when an unknown printer took a galley of type and scrambled it to make a type specimen book. It has survived not only five centuries, but also the leap into electronic typesetting, remaining essentially unchanged. It was popularised in the 1960s with the release of Typeleaf sheets containing Lorem Ipsum passages, and more recently with desktop publishing software like Quillset Layout including versions of Lorem Ipsum.</p>
        <p>Lorem Ipsum is simply dummy text of the printing and typesetting industry. Lorem Ipsum has been the industry's standard dummy text ever since the 1500s, when an unknown printer took a galley of type and scrambled it to make a type specimen book. It has survived not only five centuries, but also the leap into electronic typesetting, remaining essentially unchanged. It was popularised in the 1960s with the release of</p>
        <p>Typeleaf sheets containing Lorem Ipsum passages, and more recently with desktop publishing software like Quillset Layout including versions of Lorem Ipsum.lease of Typeleaf sheets containing Lorem Ipsum passages, and more recently with desktop publishing software like Quillset Layout including versions of Lorem Ipsum publishing software like Quillset Layout including versions of Lorem Ipsum</p>
      </div>
      <div class="signature">Mara Ellison<br>Managing Director</div>
    </div>

    <div class="footer-band">
      <div class="contact">
        <span class="item"><svg width="10" height="10" viewBox="0 0 10 10"><circle cx="5" cy="5" r="4.3" fill="none" stroke="#fff" stroke-width="1"/><path d="M3 4.2c0-.8 4-.8 4 0v.6H3z" fill="#fff"/><rect x="3.5" y="5.2" width="3" height="1.6" fill="#fff"/></svg>555-862-1907</span>
        <span class="item"><svg width="10" height="10" viewBox="0 0 10 10"><circle cx="5" cy="5" r="4.3" fill="none" stroke="#fff" stroke-width="1"/><rect x="2.8" y="3.5" width="4.4" height="3" fill="none" stroke="#fff" stroke-width=".8"/><path d="M2.8 3.5L5 5.2 7.2 3.5" fill="none" stroke="#fff" stroke-width=".8"/></svg>dale@fernhallowsigns.example</span>
      </div>
      <div class="web">www.fernhallowsigns.example</div>
    </div>
  </section>

  <!-- Business card front -->
  <section class="sheet card-front" aria-label="Business card front">
    <div class="wordmark"><span class="mark-square"></span>FERNHALLOW</div>
    <div class="card-person">
      <div class="name"><span class="first">DALE</span> FERNHALLOW</div>
      <div class="role">President</div>
    </div>
    <div class="card-contact">
      <div class="item"><svg width="6" height="6" viewBox="0 0 10 10"><circle cx="5" cy="5" r="5" fill="#0b63a0"/><rect x="3" y="4" width="4" height="2.5" fill="#fff"/></svg>555-862-1907</div>
      <div class="item"><svg width="6" height="6" viewBox="0 0 10 10"><circle cx="5" cy="5" r="5" fill="#0b63a0"/><rect x="2.8" y="3.5" width="4.4" height="3" fill="#fff"/></svg>dale@fernhallowsigns.example</div>
    </div>
    <div class="footer-band">
      <div class="contact">4873 Quarry Rd. 915 N. PO BOX 528617, Austin, TX 78519</div>
      <div class="web">fernhallowsigns.example</div>
    </div>
  </section>

  <!-- Business card back -->
  <section class="sheet card-back" aria-label="Business card back">
    <div class="wordmark on-dark"><span class="mark-square"></span>FERNHALLOW</div>
  </section>

  <!-- Envelope front -->
  <section class="sheet envelope-front" aria-label="Envelope front">
    <div class="wordmark"><span class="mark-square"></span>FERNHALLOW</div>
    <div class="address">
      <div class="company">Fernhallow Outdoor Advertising</div>
      <div>4873 Quarry Rd. 915 N. PO BOX 528617</div>
      <div>Austin, TX 78519</div>
    </div>
    <div class="footer-band">
      <div class="contact">
        <span class="item"><svg width="9" height="9" viewBox="0 0 10 10"><circle cx="5" cy="5" r="4.3" fill="none" stroke="#fff" stroke-width="1"/><rect x="3" y="4" width="4" height="2.5" fill="#fff"/></svg>555-862-1907</span>
        <span class="item"><svg width="9" height="9" viewBox="0 0 10 10"><circle cx="5" cy="5" r="4.3" fill="none" stroke="#fff" stroke-width="1"/><rect x="2.8" y="3.5" width="4.4" height="3" fill="none" stroke="#fff" stroke-width=".8"/><path d="M2.8 3.5L5 5.2 7.2 3.5" fill="none" stroke="#fff" stroke-width=".8"/></svg>dale@fernhallowsigns.example</span>
      </div>
      <div class="web">www.fernhallowsigns.example</div>
    </div>
  </section>

  <!-- Envelope back -->
  <section class="sheet envelope-back" aria-label="Envelope back">
    <svg width="487" height="242" viewBox="0 0 487 242">
      <rect x="0" y="0" width="487" height="242" fill="#e6e6e6"/>
      <path d="M8 50 L4 230 L0 242 M479 50 L483 230 L487 242" fill="none" stroke="#d2d2d2" stroke-width="1"/>
      <path d="M0 0 H487 C481 28 471 44 458 50 L262 76 Q243 80 224 76 L29 50 C16 44 6 28 0 0 Z" fill="var(--brand-blue)"/>
    </svg>
    <div class="wordmark on-blue"><span class="mark-square"></span>FERNHALLOW</div>
  </section>

</main>
</body>
</html>
```